Orbit Field Athletics - "Vuemarq of Sports" design needed

We need a web design created for Orbit Field Athletics. This includes these separate page
The Site map needed has been updated and available to you in Adobe Muse.....
1) Landing Page / Home page
2) Authentication login / Sign up page
3) After logged in - All Content Page
- IE: Vuemarq
4) Once a thumbnail is selected - Content player and other similar content thumbnails
- IE: Vuemarq
4) Generic pages for content fields - terms / policies / contact us / information / etc
5) Generic pages for customer input content fields - My profile / payment / account information / cancellation page
Important for Project Selection.....
A - Design needs to be for Desktop and Mobile.
B - The best example I can point to - that so long as skinned similarly to our
branding at OrbitFieldAthletics is vuemarq.example or KRDV MAX or Tavo
C - Final design needs to be in layered in PSD and AI
D - Attached is our old design that needs an updated concept. Format has been
done in Adobe Muse.

```html
<!DOCTYPE html>
<html lang="en">
<head>
<meta charset="utf-8">
<title>Orbit Field Athletics</title>
<link rel="stylesheet" href="https://fonts.googleapis.com/css2?family=Open+Sans:wght@400;600;700;800&display=swap">
<style>
  :root {
    --brand-red: #ec1c24;
    --ink-dark: #222222;
    --white: #ffffff;
    --sky-top: #3a3f47;
    --sky-mid: #5a6068;
    --sky-low: #4a4f57;
  }
  * { margin: 0; padding: 0; box-sizing: border-box; }
  html, body { width: 1089px; height: 1200px; overflow: hidden; background: var(--white); }
  body { position: relative; font-family: "Open Sans", Arial, sans-serif; color: var(--white); }

  .hero-photo {
    position: absolute; left: 0; top: 0; width: 1089px; height: 704px;
    background: linear-gradient(180deg, var(--sky-top) 0%, var(--sky-mid) 45%, var(--sky-low) 100%);
  }

  .account-links { position: absolute; top: 17px; right: 16px; display: flex; gap: 20px; }
  .account-links a {
    display: block; width: 79px; height: 26px; border: 2px solid var(--white); border-radius: 13px;
    color: var(--white); text-decoration: none; font-size: 12px; font-weight: 600;
    text-align: center; line-height: 22px;
  }

  .brand { position: absolute; left: 48px; top: 88px; display: flex; align-items: center; gap: 10px; }
  .brand-mark { width: 16px; height: 16px; background: var(--brand-red); }
  .brand-name { font-size: 30px; font-weight: 700; color: var(--white); letter-spacing: 0.5px; }

  .hero-copy { position: absolute; left: 0; width: 1089px; top: 220px; text-align: center; }
  .hero-headline { margin-left: 20px; font-size: 39px; font-weight: 800; line-height: 46px; }
  .hero-plans { margin-top: 24px; margin-left: 20px; font-size: 24px; font-weight: 600; }
  .register-button {
    position: absolute; left: 422px; top: 434px; width: 244px; height: 61px;
    background: var(--brand-red); border-radius: 11px; color: var(--white);
    font-size: 32px; font-weight: 600; text-align: center; line-height: 61px; text-decoration: none;
  }

  .live-games { position: absolute; left: 44px; top: 586px; width: 1002px; height: 350px; background: var(--brand-red); }
  .live-title { position: absolute; top: 24px; left: 0; width: 908px; text-align: center; font-size: 26px; font-weight: 600; }
  .carousel-arrow { position: absolute; top: 160px; width: 24px; height: 28px; }
  .carousel-arrow.prev { left: 32px; }
  .carousel-arrow.next { left: 928px; }

  .sport { position: absolute; top: 104px; width: 200px; text-align: center; }
  .sport svg { display: block; margin: 0 auto; width: 78px; height: 78px; }
  .sport-name { margin-top: 22px; font-size: 27px; font-weight: 600; line-height: 32px; }
  .view-button {
    display: block; margin: 18px auto 0; width: 102px; height: 37px; background: var(--ink-dark);
    border-radius: 6px; color: var(--white); font-size: 19px; font-weight: 600; line-height: 37px; text-decoration: none;
  }
  .sport.soccer { left: 147px; }
  .sport.basketball { left: 379px; }
  .sport.hockey { left: 596px; }

  .site-footer { position: absolute; left: 0; top: 1070px; width: 1089px; height: 130px; background: var(--ink-dark); text-align: center; }
  .footer-links { margin-top: 22px; font-size: 20px; }
  .footer-links a { color: var(--white); text-decoration: none; }
  .footer-links span { margin: 0 12px; }
  .copyright { margin-top: 40px; margin-left: 12px; font-size: 20px; }
</style>
</head>
<body>
  <div class="hero-photo" role="img" aria-label="Photo of a motocross rider mid-jump against a cloudy grey sky"></div>

  <nav class="account-links">
    <a href="#">SIGN UP</a>
    <a href="#">LOG IN</a>
  </nav>

  <div class="brand">
    <span class="brand-mark"></span>
    <span class="brand-name">Orbit Field Athletics</span>
  </div>

  <div class="hero-copy">
    <h1 class="hero-headline">Documentaries, alternative sports,<br>and more! Live and on-demand.<br>Anytime. Anywhere.</h1>
    <p class="hero-plans">Plans starting at $5.99 a month.</p>
  </div>
  <a class="register-button" href="#">REGISTER</a>

  <section class="live-games">
    <h2 class="live-title">LIVE GAMES</h2>

    <svg class="carousel-arrow prev" viewBox="0 0 24 28"><path d="M16 4 L7 14 L16 24" fill="none" stroke="#fff" stroke-width="5"/></svg>
    <svg class="carousel-arrow next" viewBox="0 0 24 28"><path d="M8 4 L17 14 L8 24" fill="none" stroke="#fff" stroke-width="5"/></svg>

    <div class="sport soccer">
      <svg viewBox="0 0 80 80">
        <circle cx="40" cy="40" r="36" fill="#fff"/>
        <circle cx="40" cy="40" r="32" fill="none" stroke="var(--brand-red)" stroke-width="3"/>
        <polygon points="40,28 51,36 47,49 33,49 29,36" fill="var(--brand-red)"/>
        <path d="M40 28 V14 M51 36 L64 31 M47 49 L55 61 M33 49 L25 61 M29 36 L16 31" stroke="var(--brand-red)" stroke-width="3"/>
        <path d="M32 10 L40 14 L48 10 M68 26 L64 31 L67 42 M60 66 L55 61 L45 70 M20 66 L25 61 L35 70 M12 26 L16 31 L13 42" fill="none" stroke="var(--brand-red)" stroke-width="3"/>
      </svg>
      <div class="sport-name">SOCCER</div>
      <a class="view-button" href="#">VIEW</a>
    </div>

    <div class="sport basketball">
      <svg viewBox="0 0 80 80">
        <circle cx="40" cy="40" r="37" fill="#fff"/>
        <g fill="none" stroke="var(--brand-red)" stroke-width="3.5">
          <path d="M14 16 Q44 30 62 70"/>
          <path d="M6 38 Q40 36 74 46"/>
          <path d="M40 3 Q56 30 77 34"/>
          <path d="M10 58 Q30 46 52 75"/>
        </g>
      </svg>
      <div class="sport-name">BASKETBALL</div>
      <a class="view-button" href="#">VIEW</a>
    </div>

    <div class="sport hockey">
      <svg viewBox="0 0 80 80">
        <ellipse cx="26" cy="26" rx="20" ry="10" fill="#fff"/>
        <path d="M6 26 V40 A20 10 0 0 0 46 40 V26" fill="#fff"/>
        <ellipse cx="26" cy="26" rx="12" ry="5" fill="var(--brand-red)"/>
        <path d="M68 2 L74 2 L58 76 L10 76 L10 62 L50 62 Z" fill="#fff"/>
        <rect x="20" y="66" width="28" height="6" fill="var(--brand-red)"/>
      </svg>
      <div class="sport-name">HOCKEY</div>
      <a class="view-button" href="#">VIEW</a>
    </div>
  </section>

  <footer class="site-footer">
    <p class="footer-links">
      <a href="#">terms of service</a><span>|</span><a href="#">privacy statement</a><span>|</span><a href="#">user agreement</a><span>|</span><a href="#">faq</a><span>|</span><a href="#">help</a>
    </p>
    <p class="copyright">©2018 Orbit Field Athletics. All rights reserved</p>
  </footer>
</body>
</html>
```